Vehicle Signage Design for a Renovation Company

We're a renovation company specialising in Home Renovations. The final design should communicate trust, credibility, and confidence. We need vehicle signage designed for our company utes (see attachment) / for our grey ute with the canopy/ and white use withou the canopyI've also attached our existing designs for the current vehicles (van and hatch back) to give you an idea of what we're after.In terms of content, there isn't much requirement for this due to the limited space on the ute - but happy to hear ideas on this.We've tried designing it ourselves - see attachment, but not happy with the result, would like more variations and ideas.Check out our website www.brightwallbuilders.co.nz for ideas on our branding/ style.

Target Market(s)

Home Owners

Industry/Entity Type

Residential Construction

Font styles to use
Sans Serif

Colors
3276b5
0355a3
33a6d7
3aa7d7
ffffff

Requirements
Must have
• Logo, Call to Action (website and number), Headline
Nice to have
• Strong sharp lines, a clean/sleek look
• It would be nice to have our offer on there (free design plans) / but we know space is limited

```html
<!DOCTYPE html>
<html lang="en">
<head>
<meta charset="utf-8">
<title>Brightwall Builders – Ute Side Signage</title>
<link rel="stylesheet" href="https://fonts.googleapis.com/css2?family=Open+Sans:wght@400;600;700;800&display=swap">
<style>
  :root {
    --bg: #ffffff;
    --panel: #e6e8eb;
    --panel-edge: #cfd3d8;
    --blue: #1f6fd6;
    --blue-deep: #0355a3;
    --navy: #0b2a8a;
    --sky: #3aa7d7;
    --red: #e0384a;
    --ink: #111418;
    --white: #ffffff;
  }
  * { margin: 0; padding: 0; box-sizing: border-box; }
  html, body { width: 1200px; height: 904px; overflow: hidden; background: var(--bg); }
  body { font-family: "Open Sans", Arial, sans-serif; position: relative; }

  .wrap-layout {
    position: absolute;
    left: 40px; top: 322px;
    width: 1120px; height: 260px;
    background: var(--panel);
    border: 1px solid var(--panel-edge);
    overflow: hidden;
  }

  .rear-panel {
    position: absolute;
    left: 0; top: 0;
    width: 340px; height: 260px;
  }
  .rear-panel .kitchen-photo {
    position: absolute; inset: 0;
    background: linear-gradient(180deg, #2f5fc9 0%, #6f8fd0 40%, #b9c4da 72%, #2a6fd6 100%);
  }
  .rear-headline {
    position: absolute;
    left: 0; top: 22px; width: 340px;
    text-align: center;
    color: var(--white);
    font-weight: 700;
    font-size: 20px;
    line-height: 27px;
    letter-spacing: 0.2px;
  }
  .offer-bar {
    position: absolute;
    left: 42px; top: 84px;
    width: 276px; height: 24px;
    background: var(--red);
    color: var(--white);
    font-size: 11.5px;
    font-weight: 400;
    line-height: 24px;
    text-align: center;
  }

  .door-panel {
    position: absolute;
    left: 340px; top: 0;
    width: 780px; height: 260px;
  }
  .tagline {
    position: absolute;
    left: 140px; top: 24px;
    color: var(--red);
    font-size: 17px;
    font-weight: 400;
    letter-spacing: 0.2px;
  }
  .brand-name {
    position: absolute;
    left: 120px; top: 60px;
    color: var(--navy);
    font-size: 56px;
    font-weight: 800;
    line-height: 1;
    letter-spacing: -0.5px;
  }
  .brand-sub {
    position: absolute;
    left: 300px; top: 132px;
    color: var(--ink);
    font-size: 20px;
    font-weight: 700;
    letter-spacing: 0.3px;
  }

  .contact-band {
    position: absolute;
    left: 0; bottom: 0;
    width: 1120px; height: 46px;
  }
  .contact-band svg { position: absolute; inset: 0; }
  .contact-phone, .contact-web {
    position: absolute;
    top: 14px;
    color: var(--white);
    font-size: 14px;
    font-weight: 700;
    letter-spacing: 0.3px;
  }
  .contact-phone { left: 418px; }
  .contact-web { left: 566px; }
</style>
</head>
<body>
  <main class="wrap-layout">
    <section class="rear-panel">
      <div class="kitchen-photo" role="img" aria-label="Photo of a bright renovated kitchen with a blue tint"></div>
      <h1 class="rear-headline">THINKING ABOUT RENOVATING<br>YOUR HOME?</h1>
      <p class="offer-bar">BOOK A FREE DESIGN TO BUILD CONSTRUCTION</p>
    </section>

    <section class="door-panel">
      <p class="tagline">TRUSTED HOME RENOVATION EXPERTS</p>
      <p class="brand-name">Brightwall Builders</p>
      <p class="brand-sub">HOME RENOVATIONS</p>
    </section>

    <footer class="contact-band">
      <svg width="1120" height="46" viewBox="0 0 1120 46" aria-hidden="true">
        <defs>
          <linearGradient id="bandFill" x1="0" y1="0" x2="1" y2="0">
            <stop offset="0" stop-color="#1f6fd6"/>
            <stop offset="1" stop-color="#2f7fe6"/>
          </linearGradient>
        </defs>
        <polygon points="0,0 1120,0 1120,20 1090,46 0,46" fill="url(#bandFill)"/>
      </svg>
      <span class="contact-phone">0800 555 014</span>
      <span class="contact-web">BRIGHTWALLBUILDERS.CO.NZ</span>
    </footer>
  </main>
</body>
</html>
```